Heartnight Soiree- The Tailored Gala

This is an elegant Dinner concert event for Valentines day February 14 2020 in Vancouver WA. Live R&B band.

Join us for an Evening of live R&B music Featuring some of Oregon and Washington's talented music artists

Tickets prices: $30 concert only pp
$60 dinner and concert pp
$90 VIP Dinner & one drink/Concert/Premium Seating/Special Gift pp
Doors open @ 6:45 Event is 7:30 to 10:30
Location: Larkspur
417 Fenwick Ave.B Vancouver, WA 98664

www.teamhollowfen.com for more info.

Target Market(s)

Adults /Couples

Industry/Entity Type

Entertainment Industry

Font styles to use
Sans Serif
Decorative

Colors

Designer to choose colors to be used in the design.

Requirements
Must have
• Add the logos for Sponsors of the Event. Brindles is the main sponsor of the event.
• Main colors should be Red and right for valentine. Needs to be sized for a 5x7 Flyer
• Include the pictures of the Music Artists

```html
<!DOCTYPE html>
<html lang="en">
<head>
<meta charset="utf-8">
<title>Heartnight Soiree- The Tailored Gala</title>
<link rel="stylesheet" href="https://fonts.googleapis.com/css2?family=Oswald:wght@300;400;500;600&family=Great+Vibes&display=swap">
<style>
  :root {
    --stage: #1c1c1c;
    --ink: #141414;
    --red: #c41a2a;
    --script: #a3101d;
    --wine: #7d0f16;
    --deep: #4a070c;
    --cream: #fbf3e6;
    --peach: #f4c9a0;
    --gold: #d9a84a;
    --gold-light: #f3d27a;
    --text-light: #f7e9d6;
  }
  * { box-sizing: border-box; margin: 0; padding: 0; }
  html, body {
    width: 983px; height: 1200px; overflow: hidden;
    background: var(--stage);
  }
  .flyer {
    position: absolute; left: 63px; top: 0;
    width: 857px; height: 1200px; overflow: hidden;
    font-family: "Oswald", sans-serif;
    text-align: center;
  }
  .flyer__backdrop {
    position: absolute; inset: 0;
    background: linear-gradient(180deg,
      var(--cream) 0%, #fffaf2 22%, #f9e4cc 36%, var(--peach) 44%,
      #e0734f 52%, var(--red) 60%, var(--wine) 78%, var(--deep) 100%);
  }
  .flyer > *:not(.flyer__backdrop) { position: absolute; left: 0; right: 0; }
  .intro {
    top: 44px; font-weight: 600; font-size: 29px; line-height: 38px;
    color: var(--ink); text-transform: uppercase; letter-spacing: .3px;
  }
  .headline {
    top: 186px; font-weight: 500; font-size: 76px; line-height: 84px;
    color: var(--red); text-transform: uppercase;
  }
  .title-script {
    top: 280px; font-family: "Great Vibes", cursive;
    font-size: 146px; line-height: 150px; color: var(--script);
  }
  .title-day {
    top: 436px; left: 596px !important; right: auto !important;
    font-weight: 400; font-size: 26px; letter-spacing: 6px; color: var(--script);
  }
  .date-line {
    top: 512px; font-weight: 400; font-size: 34px; color: var(--ink);
    text-transform: uppercase;
  }
  .artists { top: 660px; height: 180px; }
  .artist {
    position: absolute; top: 0; width: 176px; height: 176px; border-radius: 50%;
    border: 5px solid var(--gold);
    background: radial-gradient(circle at 50% 40%, #6b4a3c, #2a1814 75%);
    box-shadow: 0 4px 14px rgba(0,0,0,.45);
  }
  .artist:nth-child(1) { left: 34px; }
  .artist:nth-child(2) { left: 238px; }
  .artist:nth-child(3) { left: 443px; background: radial-gradient(circle at 50% 40%, #7b97b5, #2a3746 75%); }
  .artist:nth-child(4) { left: 647px; }
  .rule { height: 2px; background: var(--gold); opacity: .8; margin: 0 60px; }
  .rule--top { top: 880px; }
  .rule--bottom { top: 984px; }
  .tickets {
    top: 901px; height: 66px; display: flex; justify-content: center;
    color: var(--text-light); font-size: 19px; line-height: 30px; text-transform: uppercase;
    white-space: nowrap;
  }
  .tickets__col { width: 390px; text-align: left; padding: 0 16px; }
  .tickets__col--left { text-align: right; border-right: 2px solid var(--gold); }
  .details {
    top: 1002px; font-size: 14px; letter-spacing: .4px; color: var(--text-light);
    text-transform: uppercase; white-space: nowrap;
  }
  .website {
    top: 1062px; left: 286px !important; width: 284px; height: 30px;
    background: linear-gradient(90deg, var(--gold), var(--gold-light), var(--gold));
    font-weight: 600; font-size: 15px; line-height: 30px; color: var(--deep);
  }
  .sponsors {
    top: 1130px; display: flex; justify-content: center; gap: 70px; align-items: center;
  }
  .sponsor {
    font-weight: 500; font-size: 22px; color: #ffffff; text-transform: uppercase;
    display: flex; align-items: center; gap: 8px;
  }
  .sponsor__mark { width: 14px; height: 14px; background: #ffffff; }
</style>
</head>
<body>
  <main class="flyer">
    <div class="flyer__backdrop" role="img" aria-label="Soft cream staircase with a red carpet leading down into sparkling red glitter"></div>

    <p class="intro">Join us for an evening of live R&amp;B music featuring some of<br>Oregon and Washington's talented music artists</p>

    <h1 class="headline">Live R&amp;B Band</h1>
    <p class="title-script">Valentine's</p>
    <p class="title-day">DAY</p>

    <p class="date-line">February 14, 2020 in Vancouver WA</p>

    <div class="artists">
      <div class="artist" role="img" aria-label="Portrait photo of a female singer"></div>
      <div class="artist" role="img" aria-label="Portrait photo of a male vocalist"></div>
      <div class="artist" role="img" aria-label="Portrait photo of a male performer in a cap"></div>
      <div class="artist" role="img" aria-label="Portrait photo of a female vocalist"></div>
    </div>

    <div class="rule rule--top"></div>
    <div class="tickets">
      <div class="tickets__col tickets__col--left">Tickets prices: $30 concert only pp<br>$60 dinner and concert pp</div>
      <div class="tickets__col">$90 VIP dinner &amp; one drink/concert/<br>premium seating/special gift pp</div>
    </div>
    <div class="rule rule--bottom"></div>

    <p class="details">Doors open @ 6:45 Event is 7:30 to 10:30 | Location: Larkspur | 417 Fenwick Ave.B Vancouver, WA 98664</p>

    <p class="website">www.teamhollowfen.com</p>

    <div class="sponsors">
      <span class="sponsor">Cheerline</span>
      <span class="sponsor">The Marisol Fern</span>
      <span class="sponsor"><span class="sponsor__mark"></span>Brindles</span>
    </div>
  </main>
</body>
</html>
```